automotive repair and collision repair shop card

our company is called K.R Motor service we are a automotive repair company
we also do government inspections. the company information is on the cards. I would like you to use my new logo and create a new card and use the information from my old card. Good Luck!!

Industry/Entity Type

Car Repair

Contact Information for Business Card

Address: #417-15862 91 Ave, Surrey, BC V5T 8K4
Phone:(604) 555-0187
fax 604 555 0142
website www.krmotor.example

Font styles to use
Serif
Sans Serif

Requirements
Must have
• all the information
Should not have
• the owner and there name

```html
<!DOCTYPE html>
<html lang="en">
<head>
<meta charset="utf-8">
<title>K.R Motor service – Business Card</title>
<link href="https://fonts.googleapis.com/css2?family=Oswald:wght@300;400;600&display=swap" rel="stylesheet">
<style>
  :root {
    --page-bg: #e9e6e2;
    --red: #d0363f;
    --red-light: #e2565c;
    --charcoal-top: #8a8b8e;
    --charcoal-mid: #5d5e61;
    --charcoal-low: #3e3f42;
    --panel-light: #d9d9da;
    --panel-lighter: #ececec;
    --ink: #2a2a2c;
    --ink-soft: #4a4a4d;
    --black-box: #1d1d1f;
  }
  * { box-sizing: border-box; margin: 0; padding: 0; }
  html, body { width: 1200px; height: 950px; overflow: hidden; }
  body {
    background: var(--page-bg);
    font-family: "Oswald", "Arial Narrow", sans-serif;
    position: relative;
  }
  .card {
    position: absolute;
    left: 260px;
    width: 680px;
    height: 390px;
    overflow: hidden;
    border-radius: 4px;
    box-shadow: 0 10px 26px rgba(0,0,0,.22);
    background: linear-gradient(160deg, var(--charcoal-top) 0%, var(--charcoal-mid) 55%, var(--charcoal-low) 100%);
  }
  .card--front { top: 50px; }
  .card--back  { top: 510px; }

  .top-band {
    position: absolute; left: 0; top: 0; width: 100%; height: 46px;
    background: linear-gradient(90deg, var(--red) 0%, var(--red-light) 100%);
  }

  /* Brand lockup */
  .brand { position: absolute; display: flex; align-items: center; gap: 14px; }
  .brand__dot { border-radius: 50%; background: var(--ink-soft); flex: none; }
  .brand__text { display: flex; flex-direction: column; }
  .brand__name {
    font-weight: 400; color: var(--ink); text-transform: uppercase;
    letter-spacing: 1px; line-height: 1;
  }
  .brand__tagline {
    font-weight: 300; color: var(--ink); letter-spacing: .5px;
    text-align: right; line-height: 1.2;
  }

  .card--front .brand { left: 110px; top: 120px; }
  .card--front .brand__dot { width: 60px; height: 60px; }
  .card--front .brand__name { font-size: 50px; }
  .card--front .brand__tagline { font-size: 18px; margin-top: 6px; }

  .web-strip {
    position: absolute; left: 0; top: 288px; width: 100%; height: 36px;
    background: var(--panel-light);
    display: flex; align-items: center; justify-content: center;
    font-weight: 600; font-size: 20px; letter-spacing: 1px;
    color: var(--ink); text-transform: uppercase;
  }
  .red-rule {
    position: absolute; height: 2px; background: var(--red);
  }
  .card--front .red-rule { left: 0; right: 0; top: 330px; }

  /* Back */
  .placeholder-box {
    position: absolute; left: 60px; top: 110px; width: 230px; height: 70px;
    background: var(--black-box); border-radius: 8px;
  }
  .card--back .brand { right: 40px; top: 68px; }
  .card--back .brand__dot { width: 38px; height: 38px; }
  .card--back .brand__name { font-size: 30px; }
  .card--back .brand__tagline { font-size: 12px; margin-top: 4px; }

  .contact-panel {
    position: absolute; left: 0; bottom: 0; width: 100%; height: 170px;
    background: linear-gradient(180deg, var(--panel-lighter) 0%, var(--panel-light) 100%);
  }
  .contact-list {
    position: absolute; left: 28px; right: 28px; top: 38px;
    display: flex; justify-content: space-between; align-items: center;
    list-style: none;
  }
  .contact-item {
    display: flex; align-items: center; gap: 8px;
    font-weight: 600; font-size: 15px; line-height: 1.15;
    color: var(--ink); text-transform: uppercase;
  }
  .contact-item svg { width: 30px; height: 30px; flex: none; }
  .card--back .red-rule { left: 40px; right: 40px; top: 110px; }
</style>
</head>
<body>

<section class="card card--front" aria-label="Card front">
  <div class="top-band"></div>
  <div class="brand">
    <span class="brand__dot"></span>
    <div class="brand__text">
      <span class="brand__name">K.R Motor service</span>
      <span class="brand__tagline">One Stop Repair Shop</span>
    </div>
  </div>
  <div class="web-strip">www.krmotor.example</div>
  <div class="red-rule"></div>
</section>

<section class="card card--back" aria-label="Card back">
  <div class="top-band"></div>
  <div class="placeholder-box"></div>
  <div class="brand">
    <span class="brand__dot"></span>
    <div class="brand__text">
      <span class="brand__name">K.R Motor service</span>
      <span class="brand__tagline">One Stop Repair Shop</span>
    </div>
  </div>
  <div class="contact-panel">
    <ul class="contact-list">
      <li class="contact-item">
        <svg viewBox="0 0 30 30" aria-hidden="true"><rect width="30" height="30" rx="5" fill="#2a2a2c"/><path d="M15 6a6 6 0 0 0-6 6c0 4.5 6 12 6 12s6-7.5 6-12a6 6 0 0 0-6-6z" fill="#ececec"/><circle cx="15" cy="12" r="2.3" fill="#2a2a2c"/></svg>
        <span>#417-15862 91 Ave<br>Surrey, BC V5T 8K4</span>
      </li>
      <li class="contact-item">
        <svg viewBox="0 0 30 30" aria-hidden="true"><rect width="30" height="30" rx="5" fill="#2a2a2c"/><rect x="10" y="5" width="10" height="20" rx="2" fill="#ececec"/><rect x="12" y="8" width="6" height="6" fill="#2a2a2c"/><circle cx="15" cy="21" r="1.4" fill="#2a2a2c"/></svg>
        <span>(604) 555-0187</span>
      </li>
      <li class="contact-item">
        <svg viewBox="0 0 30 30" aria-hidden="true"><rect width="30" height="30" rx="5" fill="#2a2a2c"/><rect x="10" y="6" width="10" height="7" fill="#ececec"/><rect x="6" y="12" width="18" height="9" rx="2" fill="#ececec"/><rect x="10" y="18" width="10" height="6" fill="#ececec" stroke="#2a2a2c" stroke-width="1"/></svg>
        <span>604 555 0142</span>
      </li>
      <li class="contact-item">
        <svg viewBox="0 0 30 30" aria-hidden="true"><rect width="30" height="30" rx="5" fill="#2a2a2c"/><circle cx="15" cy="15" r="8" fill="none" stroke="#ececec" stroke-width="1.8"/><ellipse cx="15" cy="15" rx="3.5" ry="8" fill="none" stroke="#ececec" stroke-width="1.4"/><line x1="7" y1="15" x2="23" y2="15" stroke="#ececec" stroke-width="1.4"/></svg>
        <span>www.krmotor.example</span>
      </li>
    </ul>
    <div class="red-rule"></div>
  </div>
</section>

</body>
</html>
```